Business Card Design

Lintel Comms is a public relations consultancy service for the self build, home refurbishment and home improvement market.
It represents everything about 'home' so envisage logo featuring maybe roof pitch over the 'A' of Lintel. Colour/font undecided.

Industry/Entity Type

Home Improvement

Contact Information for Business Card

Fenella Coxworth
fenella@lintelcomms.co.uk
Telephone Direct: 0788 142 6597

```html
<!DOCTYPE html>
<html lang="en">
<head>
<meta charset="utf-8">
<title>Lintel Comms — Business Card</title>
<link rel="stylesheet" href="https://fonts.googleapis.com/css2?family=Jura:wght@600&family=Cabin:wght@400&family=Open+Sans:wght@400&display=swap">
<style>
  :root {
    --card-bg: #e9edee;
    --card-bg-edge: #dde2e3;
    --brand-brown: #4f1006;
    --name-brown: #5c1509;
    --rule-brown: #5e1409;
    --wood-dark: #7a220d;
    --wood-mid: #9a3618;
    --wood-light: #b04a26;
    --contact-ink: #2b1a15;
  }
  * { margin: 0; padding: 0; box-sizing: border-box; }
  html, body { width: 1200px; height: 668px; overflow: hidden; background: var(--card-bg); }
  .card {
    position: relative;
    width: 1200px;
    height: 668px;
    overflow: hidden;
    background: radial-gradient(ellipse at 45% 40%, var(--card-bg) 55%, var(--card-bg-edge) 100%);
  }
  .divider-rule {
    position: absolute;
    left: 0;
    top: 562px;
    width: 1200px;
    height: 6px;
    background: var(--rule-brown);
  }
  .wood-strip {
    position: absolute;
    left: 1044px;
    top: 0;
    width: 64px;
    height: 668px;
    background: linear-gradient(90deg, var(--wood-dark) 0%, var(--wood-mid) 30%, var(--wood-light) 55%, var(--wood-mid) 80%, var(--wood-dark) 100%);
  }
  .brand-name {
    position: absolute;
    left: 210px;
    top: 200px;
    font-family: "Jura", sans-serif;
    font-weight: 600;
    font-size: 104px;
    line-height: 1;
    letter-spacing: 2px;
    color: var(--brand-brown);
    white-space: nowrap;
  }
  .person-name {
    position: absolute;
    left: 74px;
    top: 466px;
    font-family: "Cabin", sans-serif;
    font-weight: 400;
    font-size: 56px;
    line-height: 1;
    color: var(--name-brown);
    white-space: nowrap;
  }
  .contact {
    position: absolute;
    top: 596px;
    font-family: "Open Sans", sans-serif;
    font-size: 24px;
    line-height: 1;
    color: var(--contact-ink);
    white-space: nowrap;
  }
  .contact-phone { left: 80px; }
  .contact-email { left: 666px; }
</style>
</head>
<body>
  <div class="card">
    <div class="divider-rule"></div>
    <div class="wood-strip" role="img" aria-label="Vertical band of reddish wood grain texture"></div>
    <div class="brand-name">Lintel Comms</div>
    <div class="person-name">Fenella Coxworth</div>
    <div class="contact contact-phone">Telephone Direct: 0788 142 6597</div>
    <div class="contact contact-email">fenella@lintelcomms.co.uk</div>
  </div>
</body>
</html>
```